Internet Of Things brochure

Need to create a brochure with a common theme to our website and the last 2 pages of the attached file. All the contect is in the file that I have attached.
website www.norvalegroup.com.au

Industry/Entity Type

Internet

```html
<!DOCTYPE html>
<html lang="en">
<head>
<meta charset="utf-8">
<title>Norvale Group – Smart Cities Initiative</title>
<link href="https://fonts.googleapis.com/css2?family=Didact+Gothic&family=Questrial&display=swap" rel="stylesheet">
<style>
  :root {
    --rust: #b8620e;
    --olive: #8a7b1c;
    --ink: #2a2a2a;
    --tan: #c8a466;
    --tan-text: #f6e7c6;
    --sky: #2fb5e6;
    --sky-pale: #d6f2f8;
  }
  * { box-sizing: border-box; margin: 0; padding: 0; }
  html, body { width: 855px; height: 1200px; overflow: hidden; }
  body {
    position: relative;
    font-family: "Didact Gothic", "Century Gothic", sans-serif;
    color: var(--ink);
    background: linear-gradient(to bottom, #ffffff 0%, #ffffff 12%, var(--sky-pale) 100%);
  }
  .band { position: absolute; left: 0; width: 855px; background: var(--rust); }
  .band--top { top: 0; height: 46px; }
  .band--bottom { top: 1154px; height: 46px; }

  .masthead { position: absolute; top: 46px; left: 0; width: 855px; height: 82px; background: #fff; }
  .brand {
    position: absolute; left: 50px; top: 22px;
    display: flex; align-items: center; gap: 8px;
    font-family: "Didact Gothic", sans-serif; font-size: 17px; line-height: 19px; color: var(--ink);
  }
  .brand__mark { width: 22px; height: 22px; background: var(--rust); flex: none; }
  .divider-v { position: absolute; top: 8px; width: 1px; height: 68px; background: var(--rust); }
  .badge { position: absolute; }
  .badge--partner { left: 164px; top: 14px; width: 150px; height: 54px; border-radius: 6px; background: #e4f3fb; }
  .badge--premier { left: 330px; top: 6px; width: 80px; height: 70px; border-radius: 4px; background: var(--sky); }
  .cloud-partner {
    position: absolute; left: 440px; top: 30px;
    font-family: "Didact Gothic", sans-serif; font-size: 20px; line-height: 22px; color: var(--ink);
  }
  .contact {
    position: absolute; left: 652px; top: 0; width: 203px; height: 82px;
    background: var(--rust); color: #fff; font-style: normal;
    font-family: "Questrial", sans-serif; font-size: 11.5px; line-height: 16px;
    text-align: right; padding: 8px 14px 0 0;
  }
  .contact__web { margin-top: 5px; }

  .intro { position: absolute; left: 52px; top: 148px; width: 754px; }
  .intro__art {
    float: left; width: 394px; height: 396px;
    background: linear-gradient(160deg, #f3e4e2 0%, #e2bdb8 60%, #f6ecea 100%);
    border-radius: 2px;
  }
  .intro__title {
    font-family: "Questrial", sans-serif; font-size: 23px; color: var(--olive);
    margin: 0 0 8px -24px; line-height: 28px;
  }
  .intro p { font-size: 16.2px; line-height: 20.1px; text-align: justify; }
  .intro p + p { margin-top: 13px; clear: both; }

  .pillars { position: absolute; left: 38px; top: 722px; width: 780px; }
  .pillar { position: absolute; width: 250px; }
  .pillar__label {
    position: absolute; left: 14px; top: 30px; width: 134px; height: 42px;
    background: var(--tan); border-radius: 14px 22px 18px 10px;
    color: var(--tan-text); font-family: "Questrial", sans-serif;
    font-size: 15px; line-height: 20px; letter-spacing: 0.5px; padding: 2px 0 0 12px;
  }
  .pillar__icon { position: absolute; left: 150px; top: 0; width: 74px; height: 66px; border-radius: 8px; }
  .pillar__bracket {
    position: absolute; left: 0; top: 54px; width: 14px; height: 148px;
    border-left: 1.5px solid var(--rust); border-top: 1.5px solid var(--rust);
  }
  .row-2 .pillar__bracket { height: 176px; }
  .pillar__text {
    position: absolute; left: 23px; top: 88px; width: 218px;
    font-size: 16px; line-height: 20px;
  }
  .col-1 { left: 0; } .col-2 { left: 264px; } .col-3 { left: 535px; }
  .row-1 { top: 0; } .row-2 { top: 223px; }
  .rule { position: absolute; left: 12px; top: 210px; width: 756px; height: 1.5px; background: var(--rust); }

  .icon--chat { background: linear-gradient(135deg, #52d6b9, #1b3f8f); }
  .icon--cart { background: linear-gradient(135deg, #5ec7e0, #d84a3a); }
  .icon--bike { background: linear-gradient(135deg, #7fb4ee, #2a5fc4); }
  .icon--tree { background: linear-gradient(135deg, #7fd23a, #5a3b22); }
  .icon--bulb { background: linear-gradient(135deg, #ffd23a, #2a64a8); }
  .icon--signal { background: linear-gradient(135deg, #c96650, #8d3528); }
</style>
</head>
<body>
  <div class="band band--top"></div>

  <header class="masthead">
    <div class="brand"><span class="brand__mark"></span><span>Norvale<br>Group</span></div>
    <div class="divider-v" style="left:155px"></div>
    <div class="badge badge--partner" role="img" aria-label="Partner business badge"></div>
    <div class="divider-v" style="left:322px"></div>
    <div class="badge badge--premier" role="img" aria-label="Premier partner badge"></div>
    <div class="divider-v" style="left:418px"></div>
    <div class="cloud-partner">Cirrus Cloud</div>
    <address class="contact">
      P: 1300 618 274<br>
      A: 41 - 43 Carrow Road<br>
      Westmead, NSW, 2145
      <div class="contact__web">W: www.norvalegroup.com.au</div>
    </address>
  </header>

  <section class="intro">
    <div class="intro__art" role="img" aria-label="Illustration of a city skyline built from small square windows"></div>
    <h1 class="intro__title">Smart Cities Initiative</h1>
    <p>A smart city is an urban development vision to integrate multiple information and communication technology (ICT) and Internet of things (IoT) solutions in a secure fashion to manage a city's assets – the city's assets include, but are not limited to, local departments' information systems, schools, libraries, transportation systems, hospitals, power plants, water supply networks, waste management, law enforcement, and other community services. The goal of building a smart city is to improve quality of life by using urban informatics and technology to improve the efficiency of services and meet residents' needs. ICT allows city officials to interact directly with the community and the city infrastructure and to monitor what is happening in the city, how the city is evolving, and how to enable a better quality of life. Through the use of sensors integrated with real-time monitoring systems, data are collected from citizens and devices – then processed and analyzed. The information and knowledge gathered are keys to tackling inefficiency. Norvale Group has the ability and smarts to push these solutions forward.</p>
    <p>Norvale Digital and Norvale Group together with the partnership of Tallon and Cirrus Cloud hosting all these systems, solutions and devices have never been easier and cost effective to deploy and capitalize on.</p>
  </section>

  <section class="pillars">
    <article class="pillar col-1 row-1">
      <div class="pillar__bracket"></div>
      <div class="pillar__label">SMART<br>GOVERNANCE</div>
      <div class="pillar__icon icon--chat" role="img" aria-label="Speech bubbles icon"></div>
      <p class="pillar__text">Interconnected within-city and across-city governance, including ICT-enabled services and interactions between public and private sectors.</p>
    </article>
    <article class="pillar col-2 row-1">
      <div class="pillar__bracket"></div>
      <div class="pillar__label">SMART<br>ECONOMY</div>
      <div class="pillar__icon icon--cart" role="img" aria-label="Globe with shopping cart icon"></div>
      <p class="pillar__text">E-business and e-commerce, ICT-enabled manufacturing and delevery of services, as well as new products, new services and business models.</p>
    </article>
    <article class="pillar col-3 row-1">
      <div class="pillar__bracket"></div>
      <div class="pillar__label">SMART<br>MOBILITY</div>
      <div class="pillar__icon icon--bike" role="img" aria-label="Bicycle icon"></div>
      <p class="pillar__text">ICT Supported and integrated transport and logistics. Sustainable, sfe and interconnected systems for public transport, cars, bicycles and pedestrians.</p>
    </article>

    <div class="rule"></div>

    <article class="pillar col-1 row-2">
      <div class="pillar__bracket"></div>
      <div class="pillar__label">SMART<br>ENVIRONMENT</div>
      <div class="pillar__icon icon--tree" role="img" aria-label="Young tree icon"></div>
      <p class="pillar__text">Smart energy including renewables, ICT-enabled energy grids, pollution control and monitoring, green buildings and green urban planning.</p>
    </article>
    <article class="pillar col-2 row-2">
      <div class="pillar__bracket"></div>
      <div class="pillar__label">SMART<br>PEOPLE</div>
      <div class="pillar__icon icon--bulb" role="img" aria-label="Light bulb icon"></div>
      <p class="pillar__text">Those with e-skills, working in ICT-enabled roles, having access to education and training, human resources and capacity management.</p>
    </article>
    <article class="pillar col-3 row-2">
      <div class="pillar__bracket"></div>
      <div class="pillar__label">SMART<br>LIVING</div>
      <div class="pillar__icon icon--signal" role="img" aria-label="Wireless signal icon"></div>
      <p class="pillar__text">ICT-enabled lifestyles, behaviour and consumption. Healthy and safe living in a culturally vibrant city with good quality housing.</p>
    </article>
  </section>

  <div class="band band--bottom"></div>
</body>
</html>
```